Business card for IT company

Looking for a business card for an IT company providing server, network, and application support to medium businesses. Company name is Halvern Systems. Website is www.halvernsystems.example, would like to use the green color that is on the homepage. Prefer design to be done in Illustrator. Please, only DESIGNERS apply - no PHP programmers attempting to do design. Thank you

Industry/Entity Type

Information Technology

Requirements
Must have
• Green
Should not have
• Template designs, or designs done by non-designer type people

```html
<!DOCTYPE html>
<html lang="en">
<head>
<meta charset="utf-8">
<title>Halvern Systems — Business Card</title>
<link href="https://fonts.googleapis.com/css2?family=Roboto:wght@300;400;700&display=swap" rel="stylesheet">
<style>
  :root {
    --brand-green: #76a435;
    --band-gray: #a9aaa9;
    --paper: #ffffff;
    --ink-gray: #555555;
    --muted-gray: #9a9a9a;
    --backdrop: #e6e6e6;
  }
  * { margin: 0; padding: 0; box-sizing: border-box; }
  html, body {
    width: 1105px;
    height: 1200px;
    overflow: hidden;
    background: var(--backdrop);
    font-family: "Roboto", Arial, sans-serif;
  }
  .sheet {
    position: relative;
    width: 1105px;
    height: 1200px;
  }
  .card {
    position: absolute;
    left: 192px;
    width: 720px;
    height: 410px;
    border-radius: 22px;
    overflow: hidden;
  }
  .card--front { top: 150px; background: var(--paper); }
  .card--back { top: 640px; background: var(--brand-green); }

  .front-art { position: absolute; inset: 0; }

  .brand {
    position: absolute;
    left: 40px;
    top: 36px;
    width: 200px;
    text-align: center;
    color: var(--paper);
  }
  .brand__mark {
    width: 116px;
    height: 116px;
    border-radius: 50%;
    background: var(--paper);
    margin: 0 auto 14px;
  }
  .brand__name {
    font-weight: 300;
    font-size: 25px;
    line-height: 1.05;
    letter-spacing: 1px;
    text-transform: uppercase;
  }

  .location {
    position: absolute;
    left: 40px;
    top: 306px;
  }
  .location__place {
    font-weight: 700;
    font-size: 25px;
    color: var(--brand-green);
  }
  .location__region {
    font-weight: 400;
    font-size: 19px;
    color: var(--muted-gray);
    margin-top: 4px;
  }

  .contact {
    position: absolute;
    right: 32px;
    top: 302px;
    list-style: none;
    text-align: right;
    color: var(--ink-gray);
  }
  .contact__item {
    display: flex;
    justify-content: flex-end;
    align-items: center;
    gap: 10px;
    height: 28px;
    font-size: 16px;
  }
  .contact__item--phone { font-size: 19px; }
  .contact__icon { width: 17px; height: 17px; flex: none; }

  .back-brand {
    position: absolute;
    left: 250px;
    top: 96px;
    width: 220px;
    height: 220px;
    border-radius: 50%;
    background: var(--paper);
    display: flex;
    align-items: center;
    justify-content: center;
    text-align: center;
    color: var(--brand-green);
    font-weight: 300;
    font-size: 28px;
    line-height: 1.1;
    letter-spacing: 1px;
    text-transform: uppercase;
  }
  .back-url {
    position: absolute;
    left: 0;
    right: 0;
    top: 338px;
    text-align: center;
    color: var(--paper);
    font-size: 18px;
    letter-spacing: 3px;
  }
</style>
</head>
<body>
<main class="sheet">

  <section class="card card--front" aria-label="Card front">
    <svg class="front-art" viewBox="0 0 720 410" width="720" height="410" aria-hidden="true">
      <path fill="var(--band-gray)" d="M0 0 H720 V236 H505 C477 236 468 244 455 258 C444 270 436 282 415 282 H0 Z"/>
      <path fill="var(--brand-green)" d="M0 0 H720 V236 H505 C475 236 465 242 452 254 C440 264 432 266 415 266 H0 Z"/>
    </svg>

    <div class="brand">
      <div class="brand__mark"></div>
      <div class="brand__name">Halvern<br>Systems</div>
    </div>

    <div class="location">
      <div class="location__place">Corvale Heights</div>
      <div class="location__region">California</div>
    </div>

    <ul class="contact">
      <li class="contact__item contact__item--phone">555.010.4821
        <svg class="contact__icon" viewBox="0 0 24 24" aria-hidden="true"><path fill="var(--brand-green)" d="M6.6 10.8a15.1 15.1 0 0 0 6.6 6.6l2.2-2.2a1 1 0 0 1 1-.25 11.4 11.4 0 0 0 3.6.57 1 1 0 0 1 1 1V20a1 1 0 0 1-1 1A17 17 0 0 1 3 4a1 1 0 0 1 1-1h3.5a1 1 0 0 1 1 1c0 1.25.2 2.45.57 3.57a1 1 0 0 1-.25 1z"/></svg>
      </li>
      <li class="contact__item">support@halvernsystems.example
        <svg class="contact__icon" viewBox="0 0 24 24" aria-hidden="true"><rect x="2" y="5" width="20" height="14" rx="1.5" fill="var(--brand-green)"/><path d="M3 6l9 7 9-7" fill="none" stroke="#fff" stroke-width="1.6"/></svg>
      </li>
      <li class="contact__item">www.halvernsystems.example
        <svg class="contact__icon" viewBox="0 0 24 24" aria-hidden="true"><circle cx="12" cy="12" r="10" fill="var(--brand-green)"/><path d="M2 12h20M12 2c3 3 3 17 0 20M12 2c-3 3-3 17 0 20" fill="none" stroke="#fff" stroke-width="1.4"/></svg>
      </li>
    </ul>
  </section>

  <section class="card card--back" aria-label="Card back">
    <div class="back-brand">Halvern<br>Systems</div>
    <div class="back-url">www.halvernsystems.example</div>
  </section>

</main>
</body>
</html>
```